FLYER FÜR VITALQUELL HAMBURG
Zielgruppe
Zielgruppe ist zwischen 30 und 45 Jahre alt und berufstätig. Mit wenig Zeit für Einkauf und Zubereitung von Speisen, aber sehr gesundheitsbewusst und sportlich.
Aufgabenstellung
Ich bräuchte einen schnellen Flyer für Vitalquell-Hamburg.com. Das Design sollte dem der Website entsprechen.
Ich habe auch eine Vorlage, die genommen werden kann, aber nicht muss.
Fotos und Texte liefere ich.
Der Flyer sollte Din hoch sein und zum aufklappen.
Ansonsten bin ich flexibel, sollte halt schön sein.
Preis inkl. MwSt, ich benötige eine Rechnung.

```html
<!DOCTYPE html>
<html lang="de">
<head>
<meta charset="utf-8">
<title>Vitalquell Hamburg – Flyer</title>
<link rel="stylesheet" href="https://fonts.googleapis.com/css2?family=Roboto+Condensed:wght@400;700&display=swap">
<style>
  :root {
    --green: #3fa535;
    --green-dark: #2f8a28;
    --white: #ffffff;
    --paper: #ffffff;
    --text-light: #eaf6e6;
    --font: "Roboto Condensed", "Arial Narrow", sans-serif;
  }
  * { box-sizing: border-box; margin: 0; padding: 0; }
  html, body { width: 1200px; height: 900px; overflow: hidden; }
  body { background: var(--paper); font-family: var(--font); color: var(--white); position: relative; }

  .panel { position: absolute; box-shadow: 0 2px 8px rgba(0,0,0,.25); overflow: hidden; }
  .photo { position: absolute; }

  /* Cover */
  .cover { left: 55px; top: 21px; width: 400px; height: 840px; background: #dcdcd6; }
  .cover-head { position: absolute; left: 0; top: 0; width: 100%; height: 272px; background: var(--green); }
  .wordmark { position: absolute; left: 48px; top: 118px; font-weight: 700; line-height: .86; text-transform: uppercase; color: var(--white); }
  .wordmark-main { display: block; font-size: 66px; letter-spacing: -1px; }
  .wordmark-sub { display: block; font-size: 49px; letter-spacing: -0.5px; }
  .cover-photo { left: 0; top: 272px; width: 100%; height: 568px;
    background: radial-gradient(circle at 45% 28%, #c8202a 0 14%, transparent 30%),
                radial-gradient(ellipse at 30% 75%, #5f7d2c 0 25%, transparent 55%),
                linear-gradient(160deg, #e6e4d8 0%, #c8b56a 28%, #8b8a3a 55%, #4e5e22 100%); }
  .cover-quote { position: absolute; left: 100px; top: 660px; font-size: 25px; font-weight: 400; text-transform: uppercase; letter-spacing: .2px; }

  /* Back panel */
  .back { left: 622px; top: 50px; width: 155px; height: 335px; background: var(--green); }
  .back .wordmark { left: 18px; top: 44px; }
  .back .wordmark-main { font-size: 24px; letter-spacing: -.3px; }
  .back .wordmark-sub { font-size: 18px; }
  .contact { position: absolute; left: 18px; top: 104px; font-size: 7px; line-height: 1.3; text-transform: uppercase; color: var(--text-light); list-style: none; }

  /* Title panel */
  .title-panel { left: 843px; top: 35px; width: 310px; height: 365px; }
  .salad-photo { inset: 0;
    background: radial-gradient(ellipse at 75% 30%, #4f8f2e 0 18%, transparent 40%),
                radial-gradient(ellipse at 55% 70%, #d0633a 0 16%, transparent 38%),
                linear-gradient(170deg, #f3f1ec 0%, #e9d9c4 45%, #c98a5e 75%, #efe7dc 100%); }
  .headline { position: absolute; font-weight: 700; text-transform: uppercase; color: var(--white); line-height: 1.12; text-align: right; }
  .title-panel .headline { right: 150px; top: 200px; font-size: 15px; }

  /* Inside spread */
  .spread { left: 714px; top: 451px; width: 446px; height: 358px; background: var(--green); display: flex; }
  .spread-col { position: relative; width: 148.7px; height: 100%; }
  .spread-col + .spread-col { border-left: 1px solid var(--green-dark); }
  .spread-col .salad-photo { inset: 0; }
  .spread-col .headline { right: 12px; top: 214px; font-size: 11px; }
  .subhead { font-size: 9.5px; font-weight: 700; text-transform: uppercase; line-height: 1.1; margin-bottom: 4px; }
  .body-copy { font-size: 6.3px; line-height: 1.32; color: var(--text-light); }
  .col-photo-top { left: 0; top: 0; width: 100%; height: 95px;
    background: linear-gradient(135deg, #eae6de 0%, #9bbd5a 35%, #d2633a 60%, #f1ece4 100%); }
  .col-block { position: absolute; left: 12px; right: 10px; }
  .bottles { left: 6px; top: 268px; width: 68px; height: 55px;
    background: linear-gradient(90deg, #e9a13a 0 20%, #b8332c 20% 40%, #d98a2e 40% 60%, #c23b2c 60% 80%, #f0eee8 80%); }
  .beside-bottles { left: 80px; right: 8px; top: 268px; }
  .dessert { left: 18px; top: 120px; width: 112px; height: 90px;
    background: radial-gradient(ellipse at 50% 45%, #f1d35a 0 14%, #f1eee6 26%, #b9a48a 60%, #7a5a3c 100%); }
  .jar { left: 12px; top: 262px; width: 46px; height: 58px;
    background: linear-gradient(180deg, #8d8f86 0%, #4d5a3c 40%, #c9c3b3 100%); }
  .beside-jar { left: 64px; right: 8px; top: 246px; }
</style>
</head>
<body>

<section class="panel cover" aria-label="Titelseite">
  <header class="cover-head">
    <h1 class="wordmark"><span class="wordmark-main">Vitalquell</span><span class="wordmark-sub">Hamburg</span></h1>
  </header>
  <div class="photo cover-photo" role="img" aria-label="Foto: rote Johannisbeeren, Minze, Mango, Banane und Ingwer im Glas"></div>
  <p class="cover-quote">„Man ist, was man isst.“</p>
</section>

<section class="panel back" aria-label="Rückseite">
  <p class="wordmark"><span class="wordmark-main">Vitalquell</span><span class="wordmark-sub">Hamburg</span></p>
  <ul class="contact">
    <li>Vitalquell Food Delivery</li>
    <li>Lindenallee 14</li>
    <li>20251 Hamburg</li>
    <li>Tel 040 55 21 64 30</li>
    <li>Fax 040 55 21 64 31</li>
    <li>www.vitalquell-hamburg.com</li>
    <li>info@vitalquell-hamburg.com</li>
  </ul>
</section>

<section class="panel title-panel" aria-label="Innentitel">
  <div class="photo salad-photo" role="img" aria-label="Foto: Salat mit Spargel, Karotten und Linsen im Glas"></div>
  <h2 class="headline">Das ist eine Headline,<br>sowieso anders.</h2>
</section>

<section class="panel spread" aria-label="Innenseiten">
  <div class="spread-col">
    <div class="photo salad-photo" role="img" aria-label="Foto: Salat mit Karotten und Linsen im Glas"></div>
    <h2 class="headline">Das ist eine Headline,<br>sowieso anders.</h2>
  </div>

  <div class="spread-col">
    <div class="photo col-photo-top" role="img" aria-label="Foto: Glasnudelsalat mit Gurke, Karotte und Chili"></div>
    <div class="col-block" style="top:104px">
      <h3 class="subhead">Das ist eine lange Subhead.</h3>
      <p class="body-copy">Frische Gerichte aus regionalen Zutaten, täglich zubereitet und direkt ins Büro geliefert. Ohne Zusatzstoffe, ohne Zucker, dafür voller Geschmack. Einfach online bestellen und entspannt genießen.</p>
    </div>
    <div class="col-block" style="top:200px">
      <h3 class="subhead">Das ist eine Subhead.</h3>
    </div>
    <div class="photo bottles" role="img" aria-label="Foto: Reihe frisch gepresster Säfte in Flaschen"></div>
    <p class="col-block body-copy beside-bottles">Kaltgepresste Säfte aus Obst und Gemüse der Saison. Jede Flasche liefert Vitamine für den ganzen Tag und passt in jede Tasche.</p>
  </div>

  <div class="spread-col">
    <div class="col-block" style="top:14px">
      <h3 class="subhead">Das ist eine lange Subhead.</h3>
      <p class="body-copy">Unsere Programme dauern drei, fünf oder sieben Tage. Sie erhalten jeden Morgen alle Mahlzeiten gekühlt an Ihre Wunschadresse und sparen Zeit beim Einkauf.</p>
    </div>
    <div class="photo dessert" role="img" aria-label="Foto: Dessert mit Mangostreifen im Glas"></div>
    <div class="col-block" style="left:64px; top:224px">
      <h3 class="subhead">Das ist eine Sub-head.</h3>
    </div>
    <div class="photo jar" role="img" aria-label="Foto: Einmachglas mit Saaten und Nüssen"></div>
    <p class="col-block body-copy beside-jar" style="top:252px">Knusprige Saaten und Nüsse als Snack für zwischendurch, abgefüllt im Glas und lange haltbar.</p>
  </div>
</section>

</body>
</html>
```